Social Media designs (LinkedIn banner, LinkedIn posts, Instagram)

Hello designers!
We are looking to create some more concepts for our social media identity for a search firm (recruitment company)
I have attached a "brand toolkit" that shows our brand, logo, colour scheme to guide you with regards to colours and identiy.

You will see in the brand toolkit there are some examples of;
- A LinkedIn banner for the company (page 23)
- Social Media posts for LinkedIn and Instagram (page 21)

What we are looking for...

We don't really like the current LinkedIn banner ideas. We would like to see more concepts that look more aesthetically pleasing - the current ideas look quite dull.

We DO like the social media post concepts but we would like to have more templates/options that we can use (similar themes)

We welcome submissions for Social Media designs that we can use with our company branding. Thank you for your work in advance!

```html
<!DOCTYPE html>
<html lang="en">
<head>
<meta charset="utf-8">
<title>Marlow Reed – Social Media Set</title>
<link href="https://fonts.googleapis.com/css2?family=Outfit:wght@300;400;500;600&display=swap" rel="stylesheet">
<style>
  :root {
    --paper: #ffffff;
    --stone: #e0e0d8;
    --stone-line: #c9c9c0;
    --brand-green: #4a8d74;
    --accent-green: #52b18c;
    --forest: #172b26;
    --ink: #111111;
    --white: #ffffff;
    --ui-line: #eeeeee;
  }
  * { margin: 0; padding: 0; box-sizing: border-box; }
  html, body { width: 1118px; height: 1200px; overflow: hidden; background: var(--paper); }
  body { position: relative; font-family: "Outfit", sans-serif; color: var(--ink); }

  .section-title { position: absolute; font-weight: 300; font-size: 24px; line-height: 1; }
  .section-title.cover-title { left: 148px; top: 150px; }
  .section-title.banner-title { left: 154px; top: 482px; }

  .cover { position: absolute; left: 149px; top: 205px; width: 778px; height: 194px; overflow: hidden; border: 1px solid var(--stone-line); }
  .cover svg { position: absolute; inset: 0; }
  .cover-tagline { position: absolute; left: 228px; top: 12px; font-weight: 300; line-height: 1; }
  .cover-tagline .small { display: block; font-size: 18px; }
  .cover-tagline .large { display: block; font-size: 32px; margin-top: 2px; }
  .cover-contact { position: absolute; left: 262px; width: 200px; top: 135px; text-align: center; color: var(--white); line-height: 1; }
  .cover-contact .label { font-size: 11px; display: block; }
  .cover-contact .phone { font-size: 16px; font-weight: 600; display: block; margin-top: 5px; }
  .cover-contact .web { font-size: 13px; font-weight: 300; display: block; margin-top: 4px; }
  .cover-name { position: absolute; left: 604px; top: 66px; color: var(--white); font-size: 28px; font-weight: 500; line-height: 1; }

  .post { position: absolute; width: 293px; height: 370px; background: var(--paper); box-shadow: 0 4px 18px rgba(0,0,0,0.08); }
  .post.job-post { left: 150px; top: 532px; }
  .post.event-post { left: 469px; top: 606px; }
  .post-header { height: 41px; display: flex; align-items: center; padding: 0 10px; gap: 6px; }
  .avatar { width: 23px; height: 23px; border-radius: 50%; background: var(--forest); }
  .handle { font-size: 10px; font-weight: 500; flex: 1; }
  .more { font-size: 12px; font-weight: 600; letter-spacing: 1px; }
  .post-art { position: relative; width: 293px; height: 292px; background: var(--forest); overflow: hidden; color: var(--white); }
  .post-footer { height: 37px; display: flex; align-items: center; padding: 0 9px; gap: 12px; }
  .post-footer .spacer { flex: 1; }

  .job-role { position: absolute; left: 14px; top: 14px; font-size: 17px; line-height: 1.1; }
  .job-role .discipline { display: block; color: var(--accent-green); }
  .job-role .place { display: block; font-size: 7px; margin-top: 3px; }
  .photo { position: absolute; }
  .post-tagline { position: absolute; left: 199px; top: 218px; font-size: 13px; font-weight: 300; line-height: 1.05; }
  .post-rule { position: absolute; height: 1px; background: var(--accent-green); }
  .post-name { position: absolute; font-weight: 500; line-height: 1; color: var(--white); }
  .job-post .post-name { left: 200px; top: 257px; font-size: 13px; }
  .event-post .post-name { left: 218px; top: 248px; font-size: 14px; }
  .event-title { position: absolute; left: 16px; top: 251px; font-size: 18px; }
</style>
</head>
<body>
  <h2 class="section-title cover-title">Linkedin Cover</h2>
  <section class="cover">
    <svg width="778" height="194" viewBox="0 0 778 194">
      <rect width="778" height="194" fill="var(--stone)"/>
      <polygon points="385,0 778,0 778,194 577,194" fill="var(--brand-green)"/>
      <path d="M254,194 L352,100 Q365,88 378,100 L475,194 Z" fill="var(--ink)"/>
      <rect x="427" y="29" width="128" height="128" rx="14" transform="rotate(45 491 93)" fill="var(--white)"/>
      <rect x="434" y="36" width="114" height="114" rx="10" transform="rotate(45 491 93)" fill="url(#skyline)" role="img" aria-label="Photo of a domed cathedral between glass towers"/>
      <defs>
        <linearGradient id="skyline" x1="0" y1="0" x2="0" y2="1">
          <stop offset="0" stop-color="#d6d8da"/>
          <stop offset="1" stop-color="#6b6f72"/>
        </linearGradient>
      </defs>
    </svg>
    <div class="cover-tagline"><span class="small">Talent knows</span><span class="large">no borders</span></div>
    <div class="cover-contact"><span class="label">CALL US</span><span class="phone">+44 0207 946 0321</span><span class="web">www.marlowreed.com</span></div>
    <div class="cover-name">Marlow<br>Reed</div>
  </section>

  <h2 class="section-title banner-title">Banner</h2>

  <article class="post job-post">
    <header class="post-header"><span class="avatar"></span><span class="handle">marlowreed</span><span class="more">···</span></header>
    <div class="post-art">
      <div class="job-role">Case Manager<span class="discipline">Enhanced Due Diligence</span><span class="place">London, United Kingdom</span></div>
      <div class="photo" style="left:0;top:126px;width:45px;height:166px;background:linear-gradient(#efe6dc,#6e6660);" role="img" aria-label="Photo of an ornate bridge column with a gilded statue"></div>
      <div class="photo" style="left:77px;top:126px;width:90px;height:166px;background:linear-gradient(#f3ede6,#7a736c);" role="img" aria-label="Photo of bridge lamps against a pale sky"></div>
      <div class="post-tagline">Talent knows<br>no borders</div>
      <div class="post-rule" style="left:199px;top:252px;width:91px;"></div>
      <div class="post-name">Marlow<br>Reed</div>
    </div>
    <footer class="post-footer">
      <svg width="20" height="20" viewBox="0 0 24 24" fill="none" stroke="#222" stroke-width="1.4"><path d="M12 20s-8-5-8-11a4 4 0 0 1 8-1 4 4 0 0 1 8 1c0 6-8 11-8 11z"/></svg>
      <svg width="20" height="20" viewBox="0 0 24 24" fill="none" stroke="#222" stroke-width="1.4"><path d="M20 12a8 8 0 1 0-3 6l3 1-1-3a8 8 0 0 0 1-4z"/></svg>
      <svg width="20" height="20" viewBox="0 0 24 24" fill="none" stroke="#222" stroke-width="1.4"><path d="M3 4l18 0-8 17-2-8z M11 13l10-9"/></svg>
      <span class="spacer"></span>
      <svg width="16" height="20" viewBox="0 0 16 20" fill="none" stroke="#222" stroke-width="1.4"><path d="M2 1h12v18l-6-5-6 5z"/></svg>
    </footer>
  </article>

  <article class="post event-post">
    <header class="post-header"><span class="avatar"></span><span class="handle">marlowreed</span><span class="more">···</span></header>
    <div class="post-art">
      <svg width="293" height="292" viewBox="0 0 293 292" style="position:absolute;inset:0">
        <rect x="81" y="0" width="57" height="62" fill="var(--brand-green)"/>
        <circle cx="305" cy="150" r="125" fill="var(--brand-green)"/>
        <circle cx="305" cy="150" r="60" fill="var(--forest)"/>
      </svg>
      <div class="photo" style="left:7px;top:62px;width:217px;height:144px;background:linear-gradient(#c9d3da,#8a8f94);" role="img" aria-label="Photo of a business team standing together in an office"></div>
      <div class="post-rule" style="left:0;top:246px;width:126px;"></div>
      <div class="event-title">Office Trip</div>
      <div class="post-rule" style="left:0;top:276px;width:96px;"></div>
      <div class="post-name">Marlow<br>Reed</div>
    </div>
    <footer class="post-footer">
      <svg width="20" height="20" viewBox="0 0 24 24" fill="none" stroke="#222" stroke-width="1.4"><path d="M12 20s-8-5-8-11a4 4 0 0 1 8-1 4 4 0 0 1 8 1c0 6-8 11-8 11z"/></svg>
      <svg width="20" height="20" viewBox="0 0 24 24" fill="none" stroke="#222" stroke-width="1.4"><path d="M20 12a8 8 0 1 0-3 6l3 1-1-3a8 8 0 0 0 1-4z"/></svg>
      <svg width="20" height="20" viewBox="0 0 24 24" fill="none" stroke="#222" stroke-width="1.4"><path d="M3 4l18 0-8 17-2-8z M11 13l10-9"/></svg>
      <span class="spacer"></span>
      <svg width="16" height="20" viewBox="0 0 16 20" fill="none" stroke="#222" stroke-width="1.4"><path d="M2 1h12v18l-6-5-6 5z"/></svg>
    </footer>
  </article>
</body>
</html>
```